Plumbing Company business card design

Create a business card for our plumbing company. Following info needs to be present

Website-prairiepipeworks.com
Email- contact@prairiepipeworks-mail.com
Phone-515-394-2068
Address-4817 NW Cobalt Blvd STE K
Ankeny, Iowa 50347

```html
<!DOCTYPE html>
<html lang="en">
<head>
<meta charset="utf-8">
<title>Prairie Pipeworks – Business Card</title>
<link rel="stylesheet" href="https://fonts.googleapis.com/css2?family=Montserrat:wght@500;700&display=swap">
<style>
  :root {
    --pipe-red: #ec2828;
    --pipe-blue: #08539b;
    --paper: #ffffff;
    --backdrop: #f4f4f4;
    --card-edge: #dedede;
  }
  html, body {
    margin: 0;
    padding: 0;
    width: 1200px;
    height: 1200px;
    overflow: hidden;
    background: var(--backdrop);
    font-family: "Montserrat", Arial, sans-serif;
  }
  .canvas {
    position: relative;
    width: 1200px;
    height: 1200px;
  }
  .card {
    position: absolute;
    left: 329px;
    width: 550px;
    height: 314px;
    background: var(--paper);
    border: 1px solid var(--card-edge);
    box-sizing: border-box;
  }
  .card--front { top: 271px; }
  .card--back { top: 674px; }

  /* Front */
  .brand-block {
    position: absolute;
    left: 0;
    right: 0;
    top: 104px;
    text-align: center;
  }
  .brand-dot {
    display: block;
    width: 40px;
    height: 40px;
    margin: 0 auto 14px;
    border-radius: 50%;
    background: var(--pipe-red);
  }
  .brand-name {
    font-weight: 700;
    font-size: 22px;
    letter-spacing: 1px;
    color: var(--pipe-blue);
    text-transform: uppercase;
    margin: 0;
  }
  .website {
    position: absolute;
    left: 0;
    right: 0;
    top: 275px;
    text-align: center;
    font-size: 9.5px;
    font-weight: 500;
    color: var(--pipe-blue);
    margin: 0;
  }

  /* Back */
  .back-brand {
    position: absolute;
    left: 34px;
    top: 120px;
    width: 226px;
    font-weight: 700;
    font-size: 30px;
    line-height: 1.1;
    color: var(--pipe-red);
    text-transform: uppercase;
    margin: 0;
  }
  .divider {
    position: absolute;
    left: 276px;
    top: 112px;
  }
  .contact-list {
    position: absolute;
    left: 318px;
    top: 124px;
    margin: 0;
    padding: 0;
    list-style: none;
    color: var(--pipe-blue);
    font-size: 12.5px;
    font-weight: 500;
    line-height: 16px;
  }
  .contact-item {
    display: flex;
    align-items: flex-start;
    gap: 8px;
  }
  .contact-icon {
    flex: none;
    width: 10px;
    height: 10px;
    margin-top: 3px;
    fill: var(--pipe-red);
  }
</style>
</head>
<body>
<main class="canvas">
  <section class="card card--front" aria-label="Card front">
    <div class="brand-block">
      <span class="brand-dot"></span>
      <p class="brand-name">Prairie Pipeworks</p>
    </div>
    <p class="website">www.prairiepipeworks.com</p>
  </section>

  <section class="card card--back" aria-label="Card back">
    <p class="back-brand">Prairie Pipeworks</p>

    <svg class="divider" width="12" height="94" viewBox="0 0 12 94" aria-hidden="true">
      <line x1="6" y1="0" x2="6" y2="94" stroke="var(--pipe-red)" stroke-width="1"/>
      <path d="M6 36 L10 47 L6 58 L2 47 Z" fill="var(--pipe-red)"/>
    </svg>

    <ul class="contact-list">
      <li class="contact-item">
        <svg class="contact-icon" viewBox="0 0 24 24" aria-hidden="true"><path d="M6.6 10.8a15 15 0 0 0 6.6 6.6l2.2-2.2a1 1 0 0 1 1-.25 11.4 11.4 0 0 0 3.6.57 1 1 0 0 1 1 1V20a1 1 0 0 1-1 1A17 17 0 0 1 3 4a1 1 0 0 1 1-1h3.5a1 1 0 0 1 1 1c0 1.25.2 2.45.57 3.57a1 1 0 0 1-.25 1z"/></svg>
        <span>515-394-2068</span>
      </li>
      <li class="contact-item">
        <svg class="contact-icon" viewBox="0 0 24 24" aria-hidden="true"><path d="M2 5h20v14H2z M2 5l10 7 10-7" /><path d="M2 5l10 7 10-7" fill="#fff" stroke="#fff" stroke-width="1.5"/></svg>
        <span>contact@prairiepipeworks-mail.com</span>
      </li>
      <li class="contact-item">
        <svg class="contact-icon" viewBox="0 0 24 24" aria-hidden="true"><path d="M12 1a7 7 0 0 0-7 7c0 5 7 13 7 13s7-8 7-13a7 7 0 0 0-7-7zm0 9.5A2.5 2.5 0 1 1 12 5.5a2.5 2.5 0 0 1 0 5z"/></svg>
        <span>4817 NW Cobalt Blvd STE K<br>Ankeny, Iowa 50347</span>
      </li>
    </ul>
  </section>
</main>
</body>
</html>
```